Velno Recycling needs a new web design

We need a new web design for our company based in Austin, TX. We resell and recycling electronics such as laptops, computer components, Tovlets, Brunos, etc. Since our inception over ten years ago, we’ve become one of the premier electronics recycling and remarketing companies in Austin, Texas.

```html
<!DOCTYPE html>
<html lang="en">
<head>
<meta charset="utf-8">
<title>Velno Recycling</title>
<link href="https://fonts.googleapis.com/css2?family=Libre+Baskerville:wght@700&family=Open+Sans:wght@400;600;700&display=swap" rel="stylesheet">
<style>
:root{
  --blue:#1670b8;
  --blue-dark:#0f5f9f;
  --orange:#f07432;
  --orange-deep:#e8632a;
  --ink:#222;
  --text:#555;
  --muted:#8a8a8a;
  --light:#f4f4f4;
  --line:#d9d9d9;
  --footer:#2e333d;
  --white:#fff;
}
*{box-sizing:border-box;margin:0;padding:0}
html,body{width:1200px;height:3285px;overflow:hidden;background:var(--white)}
body{font-family:"Open Sans",Arial,sans-serif;color:var(--text)}
.page{position:relative;width:1200px;height:3285px;overflow:hidden}
.abs{position:absolute}
.serif{font-family:"Libre Baskerville",Georgia,serif;font-weight:700}

/* header */
.site-header{left:0;top:0;width:1200px;height:92px;background:var(--white)}
.brand{left:164px;top:16px;display:flex;align-items:center;gap:10px}
.brand-dot{width:52px;height:52px;border-radius:50%;background:var(--blue)}
.brand-name{font-weight:700;font-size:26px;color:var(--blue);line-height:1}
.header-contact{top:36px;font-size:13px;color:#333}
.header-contact b{font-weight:700}
.header-divider{left:835px;top:0;width:1px;height:92px;background:var(--line)}

/* hero */
.hero{left:0;top:92px;width:1200px;height:526px;background:linear-gradient(180deg,#b9c9de 0%,#dbe3ee 55%,#eef1f5 100%)}
.main-nav{left:164px;top:92px;width:874px;height:44px;background:var(--blue);display:flex;align-items:center;padding-left:26px;gap:40px}
.main-nav a{color:var(--white);font-size:11.5px;font-weight:700;text-decoration:none;letter-spacing:.3px}
.hero-title{left:164px;top:246px;font-size:50px;color:var(--white);letter-spacing:1px}
.hero-tag{left:164px;top:302px;font-size:14px;color:var(--white);letter-spacing:5px;font-weight:600}
.hero-copy{left:164px;top:340px;width:410px;font-size:13px;line-height:20px;color:var(--white)}
.hero-devices{left:540px;top:170px;width:360px;height:310px;border-radius:50%;background:radial-gradient(circle,#7e8fa6 0%,#a9b6c9 50%,rgba(200,210,225,0) 72%)}
.hero-person{left:960px;top:190px;width:220px;height:380px;border-radius:40% 40% 30% 30%;background:linear-gradient(180deg,rgba(200,170,150,.55) 0%,#d7dbe2 55%,#f7f8fa 100%)}

/* about */
.eyebrow{font-size:11px;font-weight:700;color:var(--blue);text-align:center;letter-spacing:.5px}
.about-eyebrow{left:0;top:688px;width:1200px}
.about-title{left:0;top:702px;width:1200px;text-align:center;font-size:48px;color:var(--ink)}
.about-copy{left:0;top:766px;width:1200px;text-align:center;font-size:12.5px;line-height:24px;color:#444}
.btn{display:flex;align-items:center;justify-content:center;font-size:11px;font-weight:700;color:var(--white)}
.btn-blue{left:475px;top:828px;width:108px;height:42px;background:var(--blue)}
.btn-orange{left:598px;top:828px;width:127px;height:42px;background:var(--orange)}

/* services */
.services{left:0;top:953px;width:1200px;height:617px;background:var(--light)}
.section-title{left:0;width:1200px;text-align:center;font-size:22px;color:var(--ink)}
.services-title{top:1006px}
.title-rule{left:584px;width:32px;height:3px;background:var(--blue)}
.service-photo{top:1086px;width:254px;height:206px}
.photo-ewaste{left:258px;background:linear-gradient(160deg,#f3efdf 0%,#ddd6bf 60%,#c9c2ab 100%)}
.photo-pickup{left:679px;background:linear-gradient(180deg,#ececec 0%,#cfd3cf 45%,#8fb58a 100%)}
.service-name{top:1317px;width:300px;text-align:center;font-size:13px;font-weight:600;color:#333;letter-spacing:.3px}
.service-sub{top:1347px;width:300px;text-align:center;font-size:11.5px;font-weight:600;color:var(--blue)}
.service-copy{top:1370px;width:340px;text-align:center;font-size:11px;line-height:17.5px;color:#555}
.btn-outline{top:1470px;width:140px;height:38px;border:2px solid var(--blue);color:var(--blue);font-size:10.5px;font-weight:700;display:flex;align-items:center;justify-content:center;background:var(--white)}

/* capability */
.cap-box{background:var(--white);box-shadow:0 3px 12px rgba(0,0,0,.12);padding:18px 22px;font-size:10.5px;line-height:14.5px;color:#888}
.cap-box h3{font-size:11px;font-weight:700;color:#333;margin-bottom:6px}
.cap-box ul{list-style:none}
.cap-box li::before{content:"› ";}
.cap-recycling{left:166px;top:1682px;width:268px;height:127px;background:var(--blue);color:var(--white);box-shadow:none}
.cap-recycling h3{color:var(--white)}
.cap-recycling li{font-weight:700}
.cap-recycling li::before{content:"• "}
.cap-return{left:762px;top:1682px;width:269px;height:127px}
.cap-logistics{left:166px;top:1951px;width:268px;height:164px}
.cap-certs{left:762px;top:1951px;width:269px;height:164px}
.cap-overview{left:436px;top:1809px;width:326px;height:142px;background:var(--orange);text-align:center;color:var(--white)}
.cap-overview .eyebrow{color:var(--white);margin-top:38px}
.cap-overview .serif{font-size:40px;margin-top:2px}

/* certified */
.certified{left:0;top:2229px;width:1200px;height:482px;background:linear-gradient(135deg,var(--orange-deep) 0%,var(--orange) 50%,#ec6a2e 100%)}
.notch{left:585px;width:30px;height:15px}
.certified .eyebrow{color:var(--white)}
.certified-eyebrow{left:0;top:2338px;width:1200px}
.certified-title{left:0;top:2350px;width:1200px;text-align:center;font-size:46px;color:var(--white)}
.badge-card{top:2453px;height:147px;background:var(--white);display:flex;align-items:center;justify-content:center;box-shadow:0 4px 14px rgba(0,0,0,.2)}
.badge-a{left:182px;width:381px}
.badge-b{left:635px;width:307px}
.badge-mark{width:74px;height:74px;border-radius:50%;background:#d8dcd8}

/* contact */
.contact{left:0;top:2711px;width:1200px;height:337px;background:linear-gradient(180deg,#eceef1 0%,#dfe2e6 60%,#cfd3d8 100%)}
.contact-title{top:2790px}
.field{top:2871px;height:37px;background:var(--white);border:1px solid #bfc3c8;font-size:11px;color:#666;padding:11px 12px}
.submit{left:556px;top:2932px;width:86px;height:38px;border:2px solid var(--orange);color:var(--orange);font-size:10.5px;font-weight:700;display:flex;align-items:center;justify-content:center;background:var(--white)}

/* footer */
.site-footer{left:0;top:3048px;width:1200px;height:237px;background:var(--footer)}
.foot-heading{top:3096px;font-size:12px;font-weight:700;color:var(--white)}
.foot-text{font-size:11px;line-height:18px;color:#aab0ba}
.foot-links{left:431px;top:3126px;list-style:none;font-size:11px;line-height:21px;color:#aab0ba}
.foot-links li::before{content:"› "}
.foot-brand{left:609px;top:3123px;width:175px;height:63px;background:var(--white);display:flex;align-items:center;gap:8px;padding-left:12px}
.foot-brand .brand-dot{width:36px;height:36px}
.foot-brand .brand-name{font-size:17px}
.foot-about{left:801px;top:3108px;width:230px;font-size:10.5px;line-height:16px;color:#aab0ba}
.copyright{left:164px;top:3250px;font-size:10.5px;color:#8d94a0}
.social{top:3244px;width:24px;height:24px;border-radius:50%;border:1.5px solid #4a90c9}
</style>
</head>
<body>
<div class="page">

  <!-- header -->
  <header class="site-header abs"></header>
  <div class="brand abs"><span class="brand-dot"></span><span class="brand-name">Velno Recycling</span></div>
  <div class="header-contact abs" style="left:690px"><b>Call Us :</b> (512) 555-0148</div>
  <div class="header-divider abs"></div>
  <div class="header-contact abs" style="left:866px"><b>Email :</b> dana@velnorecycling.com</div>

  <!-- hero -->
  <section class="hero abs"></section>
  <nav class="main-nav abs">
    <a href="#">HOME</a><a href="#">ABOUT US</a><a href="#">OUR SERVICES</a><a href="#">BOOK ONLINE</a><a href="#">CONTACT US</a>
  </nav>
  <div class="hero-devices abs" role="img" aria-label="Illustration of tablets, laptops and phones circling a recycling arrows symbol"></div>
  <div class="hero-person abs" role="img" aria-label="Photo of a smiling woman sitting on a cloud pointing at the devices"></div>
  <h1 class="hero-title abs serif">COMPUTER</h1>
  <div class="hero-tag abs">RECYCLING MADE EASY</div>
  <p class="hero-copy abs">Want to make a difference to our environment and planet? Velno Recycling is here to help! Velno recycling has been helping keep the environment healthy since 2006, we specialize in recycling services that help citizens become experts at reducing waste. We have a passion to keep our world clean and are here to guide you through all the stages of the recycling process.</p>

  <!-- about -->
  <div class="eyebrow about-eyebrow abs">ABOUT</div>
  <h2 class="about-title abs serif">VELNO</h2>
  <p class="about-copy abs">What most people do not realize is electronic waste represents 2% of America's trash in landfills, but it equals 70% of overall toxic waste.<br>Used computer equipment is a rapidly growing source of waste across the country.</p>
  <a class="btn btn-blue abs">LEARN MORE</a>
  <a class="btn btn-orange abs">BOOK ONLINE</a>

  <!-- services -->
  <section class="services abs"></section>
  <h2 class="section-title services-title abs serif">SERVICES</h2>
  <div class="title-rule abs" style="top:1040px"></div>
  <div class="service-photo photo-ewaste abs" role="img" aria-label="Photo of a stack of old computers, monitors and printers"></div>
  <div class="service-photo photo-pickup abs" role="img" aria-label="Photo of keyboards in a green recycling bin"></div>
  <h3 class="service-name abs" style="left:235px">ELECTRONIC RECYCLING</h3>
  <div class="service-sub abs" style="left:235px">Environmentally Friendly</div>
  <p class="service-copy abs" style="left:215px">At Velno Recycling, we strive to keep the environment clean through our wide range of services. Our E Waste Recycling services were designed to simplify the recycling process for residents in the Austin area. Contact us today and see how you can contribute to making this world a cleaner place.</p>
  <a class="btn-outline abs" style="left:320px">SCHEDULE A PICKUP</a>
  <h3 class="service-name abs" style="left:656px">RECYCLING PICKUP</h3>
  <div class="service-sub abs" style="left:656px">We Come To You</div>
  <p class="service-copy abs" style="left:636px">At Velno Recycling, we go out of our way to make sure your recycling process is made easy as possible. Our Recycling Pickup service is designed to simplify all of your recycling needs. Take a look at all the services we offer and get in touch to see how you can start the process today!</p>
  <a class="btn-outline abs" style="left:741px">SCHEDULE A PICKUP</a>

  <!-- capability -->
  <div class="cap-box cap-recycling abs">
    <h3>RECYCLING</h3>
    <ul><li>Certified Global Recycling Capabilities</li><li>Sort by commodity</li><li>Certificate of Recycling</li><li>Data Destruction</li><li>Verifiable Certified Downstream Vendors</li></ul>
  </div>
  <div class="cap-box cap-return abs">
    <h3>RETURN:</h3>
    <ul><li>Market Value Pricing</li><li>Profit Sharing</li></ul>
  </div>
  <div class="cap-overview abs">
    <div class="eyebrow">CAPABILITY</div>
    <div class="serif">OVERVIEW</div>
  </div>
  <div class="cap-box cap-logistics abs">
    <h3>LOGISTICS</h3>
    <ul><li>Global Logistics Support</li><li>Global Warehouse Capabilities</li><li>Global Audit Capabilities</li><li>Inventory Management</li><li>Asset Management</li><li>Bill of Lading</li><li>Proof of Delivery</li><li>Transfer of Ownership (TOO)</li></ul>
  </div>
  <div class="cap-box cap-certs abs">
    <h3>CERTIFICATES</h3>
    <ul><li>R2:2013 Responsible Recycling Certified</li><li>ISO 14001:2015</li><li>OHSAS 18001:2007</li><li>State Environmental Quality Board (SEQB)</li><li>Registered Entity # RN100482716</li><li>GDPR Compliant</li><li>HIPAA Compliant</li></ul>
  </div>

  <!-- certified -->
  <section class="certified abs"></section>
  <svg class="notch abs" style="top:2229px" viewBox="0 0 30 15" aria-hidden="true"><polygon points="0,0 30,0 15,15" fill="#fff"/></svg>
  <div class="eyebrow certified-eyebrow abs">CERTIFIED</div>
  <h2 class="certified-title abs serif">WE ARE CERTIFIED</h2>
  <div class="badge-card badge-a abs"><div class="badge-mark" role="img" aria-label="Auditing registrar certification badge"></div></div>
  <div class="badge-card badge-b abs"><div class="badge-mark" role="img" aria-label="State environmental quality commission badge"></div></div>
  <svg class="notch abs" style="top:2711px" viewBox="0 0 30 15" aria-hidden="true"><polygon points="0,0 30,0 15,15" fill="#ec6a2e"/></svg>

  <!-- contact -->
  <section class="contact abs" role="img" aria-label="Faded photo of piled old computer monitors"></section>
  <h2 class="section-title contact-title abs serif">CONTACT US</h2>
  <div class="title-rule abs" style="top:2823px"></div>
  <div class="field abs" style="left:164px;width:228px">Name</div>
  <div class="field abs" style="left:401px;width:228px">Email</div>
  <div class="field abs" style="left:637px;width:401px">Message</div>
  <a class="submit abs">SUBMIT</a>

  <!-- footer -->
  <footer class="site-footer abs"></footer>
  <div class="foot-heading abs" style="left:164px">CONTACT US</div>
  <div class="foot-text abs" style="left:164px;top:3126px">4120 Marlow Ridge Blvd Austin, Texas 78757<br><br>Cell: (512) 555-0148 &nbsp;/&nbsp; Fax: (512) 555-0193<br>Toll Free: (844) 555-0172<br><br>Email: dana@velnorecycling.com</div>
  <div class="foot-heading abs" style="left:431px">COMPANY</div>
  <ul class="foot-links abs"><li>Home</li><li>About</li><li>Service</li><li>Contact</li></ul>
  <div class="foot-brand abs"><span class="brand-dot"></span><span class="brand-name">Velno Recycling</span></div>
  <p class="foot-about abs">That is one of the reasons we started Velno Recycling in 2006 to fill the void as a full service computer and electronic waste recycling "one stop shop." Since our inception over ten years ago, we've become one of the premier electronics recycling and remarketing companies in Austin.</p>
  <div class="copyright abs">© Copyright 2018 Velno. All Rights Reserved.</div>
  <span class="social abs" style="left:957px" aria-label="Social link"></span>
  <span class="social abs" style="left:986px" aria-label="Social link"></span>
  <span class="social abs" style="left:1015px" aria-label="Email link"></span>

</div>
</body>
</html>
```